Thornwell Building Company - advertisement poster

I am looking to print some canvas signs to advertise my general contracting company, Thornwell Building Company. The sign will measure 6' long x 3' high so the size should match that ratio. I already have a logo icon, which is the Letter 'A' and some trees that I would like to incorporate, see attached. I would also like the to have the following information listed:
1) phone number: 472-318-6095
2) email: thornwellbuildingcompany@mailvistra.net
3) website: thornwellbuildingcompany.com
4) Lic#5386204
5) I want to use this text: "BUILD WITH THE T-CREW!"

The ad should be relatively simple and clean. Black and Green are my company colors. I am open to creative ideas!

Target Market(s)

People looking to renovate their homes

Industry/Entity Type

Construction

Colors
59FF00
82FF00
B8FF75
E3FFCB
F4FFEA

Requirements
Must have
• Must have my company logo
Should not have
• No photos or complex graphics

```html
<!DOCTYPE html>
<html lang="en">
<head>
<meta charset="utf-8">
<title>Thornwell Building Company – Sign</title>
<link rel="stylesheet" href="https://fonts.googleapis.com/css2?family=Krona+One&family=Michroma&family=Montserrat:wght@500&display=swap">
<style>
  :root {
    --stage: #dcdcdc;
    --charcoal: #2f2e31;
    --green: #6db344;
    --white: #ffffff;
    --ink: #222124;
  }
  * { box-sizing: border-box; margin: 0; padding: 0; }
  html, body {
    width: 1200px; height: 640px; overflow: hidden;
    background: var(--stage);
  }
  .sign {
    position: absolute; left: 0; top: 20px;
    width: 1200px; height: 600px;
    background: var(--charcoal);
    overflow: hidden;
  }
  .headline {
    position: absolute; top: 48px; left: 0; width: 100%;
    text-align: center;
    font-family: "Krona One", sans-serif;
    font-size: 50px; line-height: 60px;
    color: var(--white);
    letter-spacing: 1px;
  }
  .headline .accent { color: var(--green); }

  .brand-mark {
    position: absolute; left: 558px; top: 150px;
    width: 84px; height: 84px;
    background: var(--green);
  }
  .established {
    position: absolute; top: 222px;
    width: 80px;
    font-family: "Michroma", sans-serif;
    font-size: 14px; letter-spacing: 4px;
    color: var(--white); text-align: center;
    border-top: 2px solid var(--green);
    border-bottom: 2px solid var(--green);
    padding: 4px 0 3px;
  }
  .established.left { left: 370px; }
  .established.right { left: 743px; }

  .company-name {
    position: absolute; top: 283px; left: 0; width: 100%;
    text-align: center;
    font-family: "Krona One", sans-serif;
    color: var(--white);
  }
  .company-name .main { display: block; font-size: 44px; line-height: 56px; }
  .company-name .sub { display: block; font-size: 18px; line-height: 28px; letter-spacing: 5px; }

  .phone-icon {
    position: absolute; left: 104px; top: 400px;
    width: 78px; height: 78px; border-radius: 50%;
    background: var(--white);
    border: 5px solid var(--charcoal);
    box-shadow: 0 0 0 3px var(--white);
    z-index: 2;
    display: flex; align-items: center; justify-content: center;
  }
  .phone-pill {
    position: absolute; left: 162px; top: 405px;
    width: 648px; height: 72px; border-radius: 36px;
    background: var(--green);
    font-family: "Krona One", sans-serif;
    font-size: 46px; line-height: 72px;
    color: var(--white);
    padding-left: 40px;
  }
  .license-pill {
    position: absolute; left: 800px; top: 416px;
    width: 294px; height: 50px; border-radius: 25px;
    background: var(--white);
    font-family: "Krona One", sans-serif;
    font-size: 20px; line-height: 50px;
    color: var(--ink); text-align: center;
  }

  .contact-band {
    position: absolute; left: 0; bottom: 0;
    width: 100%; height: 82px;
    background: var(--green);
    font-family: "Montserrat", sans-serif;
    font-weight: 500; font-size: 19px;
    color: var(--white);
  }
  .contact-band .email { position: absolute; left: 48px; top: 28px; }
  .contact-band .website { position: absolute; right: 48px; top: 28px; }
  .band-pointer { position: absolute; left: 548px; top: 0; }
</style>
</head>
<body>
  <main class="sign">
    <h1 class="headline">BUILD WITH THE <span class="accent">T-CREW!</span></h1>

    <div class="brand-mark" aria-hidden="true"></div>
    <div class="established left">ESTD</div>
    <div class="established right">2020</div>

    <h2 class="company-name">
      <span class="main">THORNWELL</span>
      <span class="sub">BUILDING COMPANY</span>
    </h2>

    <div class="phone-icon">
      <svg width="38" height="38" viewBox="0 0 24 24" aria-hidden="true">
        <path d="M6.6 3.5l2.6 3.3-1.6 2.2c1 2.3 3 4.3 5.4 5.4l2.2-1.6 3.3 2.6-1.4 3c-6.8-.4-12.2-5.8-12.6-12.6z"
              fill="none" stroke="#6db344" stroke-width="1.6" stroke-linejoin="round"/>
        <path d="M14 6.5a4 4 0 0 1 3.5 3.5M14 3a7.5 7.5 0 0 1 7 7"
              fill="none" stroke="#6db344" stroke-width="1.6" stroke-linecap="round"/>
      </svg>
    </div>
    <div class="phone-pill">472-318-6095</div>
    <div class="license-pill">Lic#5386204</div>

    <footer class="contact-band">
      <span class="email">thornwellbuildingcompany@mailvistra.net</span>
      <svg class="band-pointer" width="104" height="82" viewBox="0 0 104 82" aria-hidden="true">
        <polygon points="0,0 104,0 52,76" fill="#2f2e31"/>
        <polyline points="6,14 52,78 98,14" fill="none" stroke="#ffffff" stroke-width="6"/>
      </svg>
      <span class="website">www.ThornwellBuildingCompany.com</span>
    </footer>
  </main>
</body>
</html>
```